Need web design for our e-assessment company

We need a web design for our e-assessment company called Tavelo. We develop modern, web-based software for supporting the testing and examination process. The application is delivered as a SaaS solution.

The application helps our customers save time and money.

The design should communicate the following:

- Modern
- Innovation
- Security
- Performance

Attached you can find a screenshot of our application as well as some thoughts on the website.

We would like a front page as well as 1 sub page.

And lastly, one more website we draw inspiration from (on top of the ones mentioned in the attached document): http://www.plonkavery.example/
Updates

Dear all,

I have updated the description with 1 more example of websites we like as well as added that we would like a front page and a sub page.

Thanks in advance.

Best regards,

Torlak

Target Market(s)

Our target groups are higher education and awarding organisations. Decision makers are mostly men age 45+.

Industry/Entity Type

It Company

Requirements
Must have
• 1 front page and 1 sub page

```html
<!DOCTYPE html>
<html lang="en">
<head>
<meta charset="utf-8">
<title>Tavelo – Modern e-assessment</title>
<link rel="stylesheet" href="https://fonts.googleapis.com/css2?family=Open+Sans:ital,wght@0,400;0,600;0,700;1,700&display=swap">
<style>
:root{
  --orange:#f26a21;
  --blue:#1d6fb5;
  --green:#3c9a3c;
  --navy:#0c2746;
  --navy-2:#1b4f86;
  --ink:#333;
  --muted:#666;
  --brand-grey:#6a6a6a;
  --grey-band:#e9e9e9;
  --grey-soft:#f3f3f3;
  --dark-tag:#3a3a3a;
  --line:#d8d8d8;
}
*{box-sizing:border-box;margin:0;padding:0}
html,body{width:679px;height:1200px;overflow:hidden}
body{font-family:"Open Sans",Arial,sans-serif;color:var(--ink);background:#fff;font-size:8px;line-height:1.45}
.page{width:679px;height:1200px;position:relative}

/* header */
.site-header{height:58px;position:relative;border-bottom:1px solid var(--line)}
.brand{position:absolute;left:16px;top:14px;font-size:22px;font-weight:600;color:var(--brand-grey)}
.utility{position:absolute;right:16px;top:0;display:flex;gap:2px}
.utility a{display:block;color:#fff;text-decoration:none;font-size:8px;font-weight:600;padding:3px 9px;height:17px}
.u-login{background:var(--blue)}.u-trial{background:var(--green)}.u-search{background:var(--orange)}
.main-nav{position:absolute;right:16px;top:33px;display:flex;gap:2px}
.main-nav a{font-size:9px;color:var(--ink);text-decoration:none;padding:3px 8px}
.main-nav a.active{background:var(--orange);color:#fff}

/* hero */
.hero{height:242px;position:relative;background:linear-gradient(120deg,#0a2341 0%,#123a66 55%,#1e5a8f 100%);overflow:hidden}
.hero-visual{position:absolute;right:70px;top:10px;width:230px;height:232px;background:linear-gradient(160deg,#3d6f9e 0%,#25507d 60%,#143861 100%);border-radius:4px 4px 0 0;opacity:.9}
.hero-copy{position:absolute;left:38px;top:50px;width:300px}
.hero h1{font-style:italic;font-weight:700;font-size:18px;color:var(--orange);line-height:1.2;white-space:nowrap}
.hero p{color:#e6eef7;font-size:8.5px;margin-top:10px;width:250px}
.hero-actions{margin-top:14px;display:flex;flex-wrap:wrap;gap:7px;width:240px}
.btn{display:inline-block;color:#fff;font-weight:700;text-decoration:none;font-size:9px;padding:5px 14px;border-radius:2px;white-space:nowrap}
.btn-orange{background:var(--orange)}
.btn-blue{background:var(--blue)}
.btn-green{background:var(--green)}
.hero-actions .btn-blue{margin-left:40px}

/* welcome */
.welcome{height:125px;position:relative;padding:22px 16px 0 38px}
.section-title{font-style:italic;font-weight:700;font-size:16px;color:var(--orange)}
.welcome p{width:430px;margin-top:6px;color:var(--muted)}
.video{position:absolute;right:20px;top:22px;width:150px;height:88px;background:#1d1d1d;border:3px solid #444}
.video .play{position:absolute;left:60px;top:30px;width:26px;height:26px;border-radius:50%;background:var(--orange)}
.video .play svg{position:absolute;left:9px;top:7px}
.video .bar{position:absolute;left:6px;right:6px;bottom:6px;height:4px;background:#555}

/* products */
.products{height:90px;background:var(--grey-band);display:flex;justify-content:space-around;padding:12px 28px 0}
.product{width:120px;text-align:center}
.product-icon{width:40px;height:40px;margin:0 auto;display:flex;align-items:center;justify-content:center}
.pi-orange{background:var(--orange)}.pi-blue{background:var(--blue)}.pi-green{background:var(--green)}.pi-grey{background:#555}
.product-tag{display:inline-block;margin-top:8px;background:var(--dark-tag);color:#fff;font-size:8px;font-weight:600;padding:3px 9px;border-radius:2px;white-space:nowrap}
.product-tag.light{background:#fff;color:var(--ink);border:1px solid var(--line)}

/* feature grid */
.features{display:grid;grid-template-columns:1fr 1fr;height:495px}
.feature{position:relative;padding:18px 14px 0 18px;height:247px}
.feature.alt{background:var(--grey-soft)}
.feature h2{font-style:italic;font-weight:700;font-size:16px}
.t-orange{color:var(--orange)}.t-blue{color:var(--blue)}.t-green{color:var(--green)}.t-navy{color:var(--navy-2)}
.feature p{width:175px;margin-top:6px;color:var(--muted)}
.feature .more{display:block;margin-top:6px;font-size:7.5px;color:var(--blue);text-decoration:none}
.feature-art{position:absolute;right:14px;top:36px;width:120px;height:120px;border-radius:6px}
.art-sales{background:radial-gradient(circle at 45% 45%,#f7a35c,#e0457b 55%,#6d62c9)}
.art-service{background:radial-gradient(circle at 50% 45%,#f0f0f0,#d33 60%,#999)}
.art-marketing{background:radial-gradient(circle at 50% 50%,#f0b32d,#3c9a3c 55%,#2a67b0)}
.art-platform{background:radial-gradient(circle at 50% 55%,#f6b24a,#2c6fb4 55%,#1a1a1a)}
.feature-actions{position:absolute;left:18px;top:178px;width:130px;display:flex;flex-wrap:wrap;gap:5px}
.feature-actions .btn{font-size:7.5px;padding:3px 8px;text-align:center}
.feature-actions .btn-green{width:122px}

/* footer */
.site-footer{position:absolute;left:0;top:1010px;width:679px;height:190px;border-top:1px solid var(--line)}
.footer-cols{display:flex;padding:14px 18px 0;height:150px}
.footer-col{flex:1}
.footer-col h3{font-size:9px;font-weight:600;color:var(--orange)}
.footer-links{margin-top:6px;font-size:8px;color:var(--muted)}
.social{display:flex;gap:5px;margin-top:6px}
.social span{width:14px;height:14px;background:#8a8a8a;border-radius:2px}
.subscribe{display:flex;margin-top:6px}
.subscribe input{width:130px;height:18px;border:1px solid var(--line);font:inherit;font-size:8px;padding:0 5px}
.subscribe button{background:var(--orange);color:#fff;border:0;font:inherit;font-size:8px;font-weight:700;padding:0 8px;height:18px}
.cards{display:flex;gap:4px;margin-top:14px}
.cards span{width:24px;height:15px;border-radius:2px;background:#c9c9c9}
.footer-bar{position:absolute;left:0;bottom:0;width:100%;height:38px;background:var(--grey-soft);display:flex;align-items:center;gap:12px;padding:0 18px;border-top:1px solid var(--line)}
.footer-brand{font-size:12px;font-weight:600;color:var(--brand-grey)}
.copyright{font-size:7.5px;color:var(--muted)}
</style>
</head>
<body>
<div class="page">
  <header class="site-header">
    <div class="brand">Tavelo</div>
    <nav class="utility">
      <a class="u-login" href="#">Login</a>
      <a class="u-trial" href="#">Free Trial</a>
      <a class="u-search" href="#">Search</a>
    </nav>
    <nav class="main-nav">
      <a class="active" href="#">Home</a>
      <a href="#">About Us</a>
      <a href="#">Contact</a>
    </nav>
  </header>

  <section class="hero">
    <div class="hero-visual" role="img" aria-label="Hand holding a smartphone that shows assessment result charts"></div>
    <div class="hero-copy">
      <h1>Create Tavelo. Get Answers.</h1>
      <p>Secure online exams for universities and awarding bodies, delivered as a service and ready on any device you use.</p>
      <div class="hero-actions">
        <a class="btn btn-orange" href="#">View Demos »</a>
        <a class="btn btn-orange" href="#">Free Trial »</a>
        <a class="btn btn-blue" href="#">Editions &amp; pricing »</a>
      </div>
    </div>
  </section>

  <section class="welcome">
    <h2 class="section-title">Welcome to Tavelo</h2>
    <p>Tavelo builds modern web software that supports the whole testing and examination process. Authors write items, candidates sit exams in a locked browser, and markers score them online. Results are ready in minutes, not weeks, so teams save time and money while keeping every exam secure and fair.</p>
    <div class="video">
      <div class="play"><svg width="10" height="12" viewBox="0 0 10 12"><path d="M0 0L10 6L0 12Z" fill="#fff"/></svg></div>
      <div class="bar"></div>
    </div>
  </section>

  <section class="products">
    <div class="product">
      <div class="product-icon pi-orange"><svg width="22" height="22" viewBox="0 0 22 22" fill="none" stroke="#fff" stroke-width="2"><rect x="3" y="8" width="16" height="11"/><path d="M3 8L6 3H16L19 8"/></svg></div>
      <span class="product-tag light">Tavelo Examsafe</span>
    </div>
    <div class="product">
      <div class="product-icon pi-blue"><svg width="22" height="22" viewBox="0 0 22 22" fill="#fff"><rect x="3" y="12" width="4" height="7"/><rect x="9" y="8" width="4" height="11"/><rect x="15" y="4" width="4" height="15"/></svg></div>
      <span class="product-tag">Tavelo Report</span>
    </div>
    <div class="product">
      <div class="product-icon pi-green"><svg width="22" height="22" viewBox="0 0 22 22" fill="none" stroke="#fff" stroke-width="2"><rect x="6" y="2" width="10" height="18" rx="1.5"/><line x1="10" y1="17" x2="12" y2="17"/></svg></div>
      <span class="product-tag">Mobile Threat Report</span>
    </div>
    <div class="product">
      <div class="product-icon pi-grey"><svg width="22" height="22" viewBox="0 0 22 22" fill="none" stroke="#fff" stroke-width="2"><path d="M11 2L21 19H1Z"/><line x1="11" y1="8" x2="11" y2="13"/><line x1="11" y1="15.5" x2="11" y2="16.5"/></svg></div>
      <span class="product-tag">Tavelo Threat Report</span>
    </div>
  </section>

  <section class="features">
    <article class="feature">
      <h2 class="t-orange">Tavelo Sales</h2>
      <p>Plan and sell exam packages with clear editions and pricing. Track every offer, licence and renewal in one place, and give each customer a tailored trial.</p>
      <a class="more" href="#">View more</a>
      <div class="feature-art art-sales" role="img" aria-label="Colourful illustration of shopping bags and a smartphone"></div>
      <div class="feature-actions"><a class="btn btn-orange" href="#">View Demo</a><a class="btn btn-blue" href="#">Free Trial</a><a class="btn btn-green" href="#">Editions &amp; Pricing</a></div>
    </article>
    <article class="feature alt">
      <h2 class="t-blue">Tavelo Service</h2>
      <p>Support staff and candidates before, during and after each exam. Live status, quick answers and a full audit trail keep every session calm and secure.</p>
      <a class="more" href="#">View more</a>
      <div class="feature-art art-service" role="img" aria-label="Illustration of a figure holding a wrench beside a rising bar chart"></div>
      <div class="feature-actions"><a class="btn btn-orange" href="#">View Demo</a><a class="btn btn-blue" href="#">Free Trial</a><a class="btn btn-green" href="#">Editions &amp; Pricing</a></div>
    </article>
    <article class="feature alt">
      <h2 class="t-green">Tavelo Marketing</h2>
      <p>Reach institutions with clear reports on results and trends. Share the value of digital exams with boards, deans and examiners in plain figures.</p>
      <a class="more" href="#">View more</a>
      <div class="feature-art art-marketing" role="img" aria-label="Illustration of figures with a megaphone and a pie chart"></div>
      <div class="feature-actions"><a class="btn btn-orange" href="#">View Demo</a><a class="btn btn-blue" href="#">Free Trial</a><a class="btn btn-green" href="#">Editions &amp; Pricing</a></div>
    </article>
    <article class="feature">
      <h2 class="t-navy">Tavelo Platform</h2>
      <p>One fast platform for authoring, delivery, marking and results. Hosted in secure data centres and built to scale from a single class to a nation.</p>
      <a class="more" href="#">View more</a>
      <div class="feature-art art-platform" role="img" aria-label="Illustration of a growing bar chart with an arrow"></div>
      <div class="feature-actions"><a class="btn btn-orange" href="#">View Demo</a><a class="btn btn-blue" href="#">Free Trial</a><a class="btn btn-green" href="#">Editions &amp; Pricing</a></div>
    </article>
  </section>

  <footer class="site-footer">
    <div class="footer-cols">
      <div class="footer-col">
        <h3>Navigation</h3>
        <div class="footer-links">Home | Tools | About | News | Contact</div>
      </div>
      <div class="footer-col">
        <h3>Follow Us</h3>
        <div class="social"><span></span><span></span><span></span><span></span><span></span><span></span></div>
      </div>
      <div class="footer-col">
        <h3>Subscribe to Our Newsletter</h3>
        <div class="subscribe"><input type="text" placeholder="Your email"><button type="button">SUBSCRIBE</button></div>
        <div class="cards"><span></span><span></span><span></span><span></span><span></span><span></span></div>
      </div>
    </div>
    <div class="footer-bar">
      <div class="footer-brand">Tavelo</div>
      <div class="copyright">© 2014 Tavelo, Inc. All rights reserved.</div>
    </div>
  </footer>
</div>
</body>
</html>
```